Gutschein-Design für Tätowierer
Sehr kompetenter Designer alles schnell und zügig erledigt. war super zufrieden mit ihm :)
Zielgruppe
Ich bin ein Tätowierer und suche ein hochwertiges Design, meine Zielgruppe sind Leute jeden Alters
Aufgabenstellung
-Farbe auf meiner Karte sollte wie bei meiner Webseite www.brenner-ink.de sein Pazifikblau/ Marineblau
-Es soll schlicht sein
-mein Logo soll auf die Vorderseite mittig (in schwarz)
-ein Rand soll enthalten sein in einem blauton
-auf die Rückseite sollen Felder zum ausfüllen sein wie zum Beispiel Name, Gutschein wert usw..
-Maße ca. 21 x 10,5 cm

```html
<!DOCTYPE html>
<html lang="de">
<head>
<meta charset="utf-8">
<title>Gutschein – Brenner Ink</title>
<link rel="stylesheet" href="https://fonts.googleapis.com/css2?family=Inter:wght@600;700&family=Kaushan+Script&display=swap">
<style>
  :root {
    --page-bg: #3a3634;
    --card-front: #2b2625;
    --card-back: #050505;
    --ink-white: #ffffff;
    --label-grey: #3b3b3b;
    --accent-blue: #2f6b86;
    --photo-dark: #1f1c1b;
    --photo-mid: #5a5452;
    --photo-light: #c9c9c9;
  }
  * { box-sizing: border-box; margin: 0; padding: 0; }
  html, body { width: 1200px; height: 800px; overflow: hidden; }
  body {
    background: var(--page-bg);
    font-family: "Inter", Arial, sans-serif;
    position: relative;
  }
  .voucher-card {
    position: absolute;
    left: 240px;
    width: 720px;
    height: 360px;
    overflow: hidden;
    box-shadow: 0 10px 30px rgba(0,0,0,.35);
  }
  /* Front */
  .voucher-front { top: 25px; background: var(--card-front); }
  .front-photo {
    position: absolute; right: 0; top: 0; width: 360px; height: 100%;
    background: linear-gradient(90deg, var(--card-front) 0%, #3f3a38 35%, var(--photo-mid) 70%, #8a8583 100%);
  }
  .front-title {
    position: absolute; left: 80px; top: 110px;
    font-family: "Kaushan Script", cursive;
    font-size: 132px; line-height: 1;
    color: var(--ink-white);
    transform: rotate(-6deg);
  }
  .brand-mark {
    position: absolute; right: 40px; top: 30px;
    display: flex; align-items: center; gap: 10px;
  }
  .brand-mark-circle {
    width: 44px; height: 44px; border-radius: 50%;
    border: 3px solid var(--ink-white);
  }
  .brand-mark-name {
    font-weight: 700; font-size: 22px; color: var(--ink-white);
  }
  /* Back */
  .voucher-back { top: 415px; background: var(--card-back); }
  .back-photo {
    position: absolute; left: 0; top: 0; width: 420px; height: 100%;
    background: linear-gradient(90deg, var(--photo-light) 0%, #9a9a9a 40%, #555 75%, var(--card-back) 100%);
  }
  .contact-row {
    position: absolute; left: 380px; top: 26px;
    display: flex; gap: 26px; align-items: center;
  }
  .contact-item {
    display: flex; align-items: center; gap: 8px;
    color: var(--ink-white); font-weight: 600; font-size: 15px;
  }
  .contact-dot {
    width: 24px; height: 24px; border-radius: 50%;
    background: var(--accent-blue);
  }
  .fill-fields {
    position: absolute; left: 390px; top: 82px; width: 300px;
    display: flex; flex-direction: column; gap: 24px;
  }
  .fill-field {
    height: 60px; background: var(--ink-white);
    display: flex; align-items: center; padding-left: 26px;
    font-weight: 700; font-size: 15px; color: var(--label-grey);
  }
</style>
</head>
<body>
  <section class="voucher-card voucher-front">
    <div class="front-photo" role="img" aria-label="Schwarzweißfoto eines Tätowierers bei der Arbeit mit Handschuhen"></div>
    <h1 class="front-title">Gutschein</h1>
    <div class="brand-mark">
      <span class="brand-mark-circle"></span>
      <span class="brand-mark-name">Brenner Ink</span>
    </div>
  </section>

  <section class="voucher-card voucher-back">
    <div class="back-photo" role="img" aria-label="Schwarzweißfoto eines Tattoo-Motivs einer Skulptur auf der Haut neben der Vorlage"></div>
    <div class="contact-row">
      <div class="contact-item"><span class="contact-dot"></span>brenner_ink</div>
      <div class="contact-item"><span class="contact-dot"></span>www.brenner-ink.de</div>
    </div>
    <div class="fill-fields">
      <div class="fill-field">Betrag :</div>
      <div class="fill-field">Für :</div>
      <div class="fill-field">Gültig Bis :</div>
    </div>
  </section>
</body>
</html>
```